Tobin Quartz Portal Page . It's guarantee project!

We need a clean and professional modern web application portal page
That includes the Login & Application Selection screen

Also, I need to design both Desktop and Mobile sizes.
We have an example design for our target

The application is Jetty Schedule and related data.
Our client is a bit conservative.

Theme color preferred : #00508B (main) #DF0D83 (secondary)

Target Market(s)

Oil & Fuel & Gasoline

Number of Pages Required

2 page

Font styles to use
Sans Serif

Colors
0054AA
0677BA
7BADD7
CADEEF
E8F1F8
E54698
E96AAD
F1A4CE
F9D9EA
FCEFF6

Requirements
Must have
• Login Page & Main Screen

```html
<!DOCTYPE html>
<html lang="en">
<head>
<meta charset="utf-8">
<title>Tobin Quartz Portal</title>
<link rel="stylesheet" href="https://fonts.googleapis.com/css2?family=Montserrat+Alternates:wght@400;500;600;700&display=swap">
<style>
  :root {
    --brand: #00508B;
    --ink: #1E1E24;
    --muted: #5F6B7A;
    --page: #F0F4F9;
    --surface: #FFFFFF;
    --line: #D9DEE5;
    --tab-bg: #EEF6FD;
    --button-bg: #E0EEFB;
    --art-pink: #FCC9EE;
    --art-blue: #DDEEFD;
    --avatar: #C9CED6;
  }
  * { box-sizing: border-box; margin: 0; padding: 0; }
  html, body {
    width: 1200px; height: 853px; overflow: hidden;
    background: var(--page);
    font-family: "Montserrat Alternates", sans-serif;
    color: var(--ink);
  }
  .topbar {
    height: 67px; background: var(--surface);
    border-bottom: 1px solid var(--line);
    display: flex; align-items: stretch;
    padding: 0 28px;
  }
  .brand-name {
    align-self: center;
    font-size: 20px; font-weight: 700; color: var(--brand);
    width: 160px;
  }
  .nav-tab {
    margin-left: 0;
    width: 76px; display: flex; align-items: center; justify-content: center;
    background: var(--tab-bg); color: var(--brand);
    font-size: 12px; font-weight: 500;
    border-bottom: 2px solid var(--brand);
  }
  .user-menu {
    margin-left: auto; display: flex; align-items: center; gap: 10px;
  }
  .user-avatar { width: 27px; height: 27px; border-radius: 50%; background: var(--avatar); }
  .user-info { width: 84px; }
  .user-name { font-size: 12px; font-weight: 600; line-height: 14px; }
  .user-email { font-size: 9.5px; color: var(--muted); line-height: 12px; }
  .user-toggle { width: 14px; height: 14px; margin-left: 6px; }
  .content { padding: 52px 90px 0; }
  .greeting { font-size: 28px; font-weight: 700; line-height: 34px; }
  .greeting-sub { font-size: 12px; margin-top: 4px; }
  .app-grid { display: flex; gap: 20px; margin-top: 26px; }
  .app-card {
    width: 327px; height: 326px; background: var(--surface);
    border-radius: 11px; padding: 20px;
    display: flex; flex-direction: column;
  }
  .app-art {
    height: 171px; border-radius: 7px;
    background: radial-gradient(ellipse 72% 95% at 50% 100%, var(--art-blue) 0 70%, var(--art-pink) 70.5%);
  }
  .app-title { font-size: 18px; font-weight: 700; margin-top: 13px; line-height: 22px; }
  .app-desc { font-size: 11.5px; color: var(--muted); line-height: 14.5px; margin-top: 3px; }
  .app-action {
    margin-top: auto; align-self: flex-end;
    width: 126px; height: 37px; border-radius: 3px;
    background: var(--button-bg); color: var(--brand);
    font: 600 12.5px "Montserrat Alternates", sans-serif;
    border: none; display: flex; align-items: center; justify-content: center;
  }
</style>
</head>
<body>
  <header class="topbar">
    <div class="brand-name">Tobin Quartz</div>
    <nav class="nav-tab">Home</nav>
    <div class="user-menu">
      <div class="user-avatar"></div>
      <div class="user-info">
        <div class="user-name">Mara Lindqvist</div>
        <div class="user-email">maralind@exa...</div>
      </div>
      <svg class="user-toggle" viewBox="0 0 14 14"><path d="M2 4.5l5 5 5-5" fill="none" stroke="#1E1E24" stroke-width="1.6" stroke-linecap="round" stroke-linejoin="round"/></svg>
    </div>
  </header>
  <main class="content">
    <h1 class="greeting">Hello, Mara!</h1>
    <p class="greeting-sub">Complete all important actions from this page.</p>
    <section class="app-grid">
      <article class="app-card">
        <div class="app-art" role="img" aria-label="Illustration of a worker with a clipboard beside stacked cargo boxes"></div>
        <h2 class="app-title">Jetty Planning</h2>
        <p class="app-desc">Lorem ipsum dolor sit amet consectetur.<br>Id ullamcorper egestas cursus amet.</p>
        <a class="app-action">Learn More</a>
      </article>
      <article class="app-card">
        <div class="app-art" role="img" aria-label="Illustration of a person in a chair tracking a parcel on a map"></div>
        <h2 class="app-title">Jetty Tracking</h2>
        <p class="app-desc">Lorem ipsum dolor sit amet consectetur.<br>Id ullamcorper egestas cursus amet.</p>
        <a class="app-action">Learn More</a>
      </article>
      <article class="app-card">
        <div class="app-art" role="img" aria-label="Illustration of a worker on a radio beside cargo lifted by a crane hook"></div>
        <h2 class="app-title">Jetty Port Performance</h2>
        <p class="app-desc">Lorem ipsum dolor sit amet consectetur.<br>Id ullamcorper egestas cursus amet.</p>
        <a class="app-action">Learn More</a>
      </article>
    </section>
  </main>
</body>
</html>
```